Social Media Beitrag (Stelle)
Alles perfekt, sehr unkomplizierte Zusammenarbeit. Schnell ein passendes Design gefunden. Die Vorstellungen wurden super entgegengenommen und umgesetzt.
Zielgruppe
Wir sind eine allgemeinmedizinischen Tierklinik, welche Unterstützung im Team sucht. Aus diesem Grund ist die Zielgruppe bei dieser Arbeit potentielle Mitarbeiter.
Aufgabenstellung
Wir möchten gerne einen Social-Media-Beitrag beispielsweise auf Pixelbrunn und Kontaktwand machen und deshalb das Stelleninserat (im Anhang) in anderer verkürzter ansprechender Art darstellen. Ich stelle mir vor die Message auf ca. 3-4 quadratischen Bilder darzustellen, dass der Leser diese nacheinander ansehen kann und direkt angesprochen wird. Es muss nicht alles vom Stelleninserat mit eingebaut werden, sondern nur das wichtigste. Bei Pixelbrunn wäre ideale Größe für quadratische Posts ist 1080 px x 1080 px mit einem Seitenverhältnis von 1:1. Wir sind jedoch für andere Ideen offen oder wenn ihr auch das Gefühl habt wir packen die Message auf ein Bild. Ziel ist es möglichst ein breites Publikum online ansprechen zu können. Das Corporate Design der Unternehmung sollte auch mit berücksichtigt werden. Das Design sollte im Indesign oder Photoshop erstellt werden, damit wir es selbständig überarbeiten oder erweitern können.
Ich möchte keine BildVorrat-Personen auf den Post abbilden, dass wirkt zu künstlich, da es nicht die richtigen Mitarbeiter sind. Vielleicht kann auch etwas mit wenig Bild oder gar kein Bild und einfach einem Icon dargestellt werden.

```html
<!DOCTYPE html>
<html lang="de">
<head>
<meta charset="utf-8">
<title>Talberg Tierarzt – Stelle Empfang TPA</title>
<link rel="stylesheet" href="https://fonts.googleapis.com/css2?family=Josefin+Sans:wght@400&family=Caveat+Brush&family=Source+Sans+3:wght@400;600&display=swap">
<style>
  :root {
    --bg-grey: #8a8a8a;
    --photo-dark: #141414;
    --photo-mid: #3a3a3a;
    --band-dark: rgba(38, 38, 38, 0.92);
    --band-crimson: #c2154a;
    --text-light: #ececec;
    --text-white: #ffffff;
  }
  * { margin: 0; padding: 0; box-sizing: border-box; }
  html, body {
    width: 1200px;
    height: 1200px;
    overflow: hidden;
    background: var(--bg-grey);
  }
  .post {
    position: relative;
    width: 1200px;
    height: 1200px;
    overflow: hidden;
    background: var(--bg-grey);
  }
  .hero-photo {
    position: absolute;
    inset: 0;
    background:
      radial-gradient(ellipse 48% 58% at 62% 52%, var(--photo-dark) 0%, var(--photo-dark) 55%, var(--photo-mid) 78%, rgba(138,138,138,0) 100%),
      var(--bg-grey);
  }
  .brand-band {
    position: absolute;
    left: 59px;
    top: 516px;
    width: 1088px;
    height: 94px;
    background: var(--band-dark);
    display: flex;
    align-items: center;
    padding-left: 16px;
  }
  .brand-name {
    font-family: "Josefin Sans", sans-serif;
    font-weight: 400;
    font-size: 62px;
    line-height: 1;
    letter-spacing: 1px;
    color: var(--text-light);
    padding-top: 10px;
  }
  .claim-band {
    position: absolute;
    left: 59px;
    top: 610px;
    width: 1088px;
    height: 166px;
    background: var(--band-crimson);
    display: flex;
    align-items: center;
    justify-content: center;
    overflow: hidden;
  }
  .claim {
    font-family: "Caveat Brush", cursive;
    font-size: 78px;
    line-height: 1;
    color: var(--text-white);
    white-space: nowrap;
    transform: rotate(-2deg);
  }
  .job-box {
    position: absolute;
    left: 68px;
    top: 1063px;
    width: 1087px;
    height: 137px;
    background: var(--band-dark);
    padding: 14px 0 0 22px;
    overflow: hidden;
  }
  .job-title {
    display: flex;
    justify-content: space-between;
    align-items: baseline;
    width: 1040px;
    font-family: "Josefin Sans", sans-serif;
    font-weight: 400;
    font-size: 46px;
    line-height: 54px;
    letter-spacing: 1px;
    color: var(--text-light);
    white-space: nowrap;
    padding-top: 4px;
  }
  .job-title .workload {
    font-family: "Source Sans 3", sans-serif;
    font-weight: 600;
    font-size: 48px;
    letter-spacing: 0;
  }
  .job-contact {
    font-family: "Source Sans 3", sans-serif;
    font-weight: 400;
    font-size: 53px;
    line-height: 56px;
    color: var(--text-light);
    white-space: nowrap;
    margin-top: 4px;
  }
</style>
</head>
<body>
  <main class="post">
    <div class="hero-photo" role="img" aria-label="Schwarzweissfoto eines schwarzen Mopses im Strickpullover vor grauem Hintergrund"></div>

    <div class="brand-band">
      <span class="brand-name">TALBERG TIERARZT</span>
    </div>

    <div class="claim-band">
      <p class="claim">Sucht Helfer mit Herz und Verstand</p>
    </div>

    <div class="job-box">
      <p class="job-title"><span>MITARBEITER/IN</span><span>EMPFANG</span><span>TPA</span><span class="workload">(80-100%)</span></p>
      <p class="job-contact">Wir freuen uns auf Ihren Anruf +41 41 555 01 23</p>
    </div>
  </main>
</body>
</html>
```